Velmarcoteni Business cards

Dear team, I need to get the design file to suit it to our team. The focus of the business card is the Automotive Market and the design must be in black colour and the logo must be in glossy black. On the front of the card I need to get the following info:

- Name and Surname
- Title
- eMail
- Phone Number
- Skype account
- domain address

```html
<!DOCTYPE html>
<html lang="es">
<head>
<meta charset="utf-8">
<title>Velmarcoteni – Business cards</title>
<link rel="stylesheet" href="https://fonts.googleapis.com/css2?family=Montserrat:wght@400;500;700;800&display=swap">
<style>
  :root {
    --stage: #2b2b2c;
    --card: #252526;
    --card-back: #1c1c1d;
    --pattern-light: #6a6a6c;
    --pattern-dark: #161617;
    --red: #e2252b;
    --white: #ffffff;
    --grey: #d9d9d9;
  }
  * { box-sizing: border-box; margin: 0; padding: 0; }
  html, body { width: 1200px; height: 1186px; overflow: hidden; }
  body {
    background: var(--stage);
    font-family: "Montserrat", sans-serif;
    position: relative;
  }
  .card {
    position: absolute;
    left: 150px;
    width: 900px;
    height: 514px;
    border-radius: 26px;
    overflow: hidden;
  }
  .card-back {
    top: 40px;
    background: var(--card-back);
  }
  .back-pattern {
    position: absolute;
    inset: 0;
    background: linear-gradient(120deg, var(--pattern-light) 0%, #2e2e30 45%, var(--pattern-dark) 100%);
  }
  .back-accent {
    position: absolute;
    right: 130px;
    top: 200px;
    width: 70px;
    height: 70px;
    background: var(--red);
  }
  .card-front {
    top: 622px;
    background: var(--card);
  }
  .brand {
    position: absolute;
    left: 70px;
    top: 130px;
    display: flex;
    align-items: center;
    gap: 24px;
    white-space: nowrap;
  }
  .brand-square {
    width: 90px;
    height: 90px;
    background: var(--red);
    flex: none;
  }
  .brand-name {
    font-weight: 800;
    font-size: 74px;
    letter-spacing: -2px;
    color: var(--white);
    line-height: 1;
  }
  .brand-tld {
    font-size: 32px;
    letter-spacing: 0;
  }
  .holder {
    position: absolute;
    right: 470px;
    top: 300px;
    text-align: right;
    white-space: nowrap;
  }
  .holder-name {
    color: var(--red);
    font-weight: 700;
    font-size: 26px;
    letter-spacing: 1px;
    text-transform: uppercase;
  }
  .holder-title {
    color: var(--white);
    font-size: 20px;
    font-weight: 500;
    margin-top: 2px;
  }
  .holder-address {
    color: var(--white);
    font-size: 18px;
    line-height: 1.35;
    margin-top: 18px;
  }
  .divider {
    position: absolute;
    left: 458px;
    top: 298px;
    width: 2px;
    height: 120px;
    background: var(--red);
  }
  .contacts {
    position: absolute;
    left: 486px;
    top: 296px;
    list-style: none;
  }
  .contacts li {
    display: flex;
    align-items: center;
    gap: 12px;
    color: var(--grey);
    font-size: 18px;
    line-height: 30px;
    white-space: nowrap;
  }
  .contacts svg { width: 16px; height: 16px; flex: none; fill: var(--red); }
</style>
</head>
<body>

<section class="card card-back" aria-label="Reverso de la tarjeta">
  <div class="back-pattern" role="img" aria-label="Patrón decorativo brillante en negro con el símbolo de la marca repetido"></div>
  <div class="back-accent"></div>
</section>

<section class="card card-front" aria-label="Anverso de la tarjeta">
  <div class="brand">
    <div class="brand-square"></div>
    <div class="brand-name">Velmarcoteni<span class="brand-tld">.com</span></div>
  </div>

  <div class="holder">
    <p class="holder-name">Dario Lentisco</p>
    <p class="holder-title">Comercial</p>
    <p class="holder-address">Pol. Ind. Norvela C/4 nº 22<br>41900 Villa Ostrena</p>
  </div>

  <div class="divider"></div>

  <ul class="contacts">
    <li>
      <svg viewBox="0 0 16 16"><path d="M3 1h3l1.5 4-2 1.3a9 9 0 0 0 4.2 4.2L11 8.5l4 1.5v3a2 2 0 0 1-2 2A12 12 0 0 1 1 3a2 2 0 0 1 2-2z"/></svg>
      600 12 34 56
    </li>
    <li>
      <svg viewBox="0 0 16 16"><path d="M1 3h14v10H1z"/><path d="M1.5 3.5l6.5 5.5 6.5-5.5" fill="none" stroke="var(--card)" stroke-width="1.3"/></svg>
      redazione@velmarcoteni.com
    </li>
    <li>
      <svg viewBox="0 0 16 16"><circle cx="8" cy="8" r="7"/></svg>
      @velmarcoteni
    </li>
    <li>
      <svg viewBox="0 0 16 16"><circle cx="8" cy="8" r="7"/><path d="M1 8h14M8 1c3 3 3 11 0 14M8 1c-3 3-3 11 0 14" fill="none" stroke="var(--card)" stroke-width="1.2"/></svg>
      www.velmarcoteni.com
    </li>
  </ul>
</section>

</body>
</html>
```